IT’S NOT A CLEANING, IT’S YOUR LIFE! TOP TEN REASONS WHY THIS IS NOT JUST A “CLEANING”

We made a list for our patients to let them know why our hygiene appointments are different than other cleanings. Since this is a lot of information, we would like it easily readable within 4-5 feet but we do not want the post to be HUGE. Please see below:

IT’S NOT A CLEANING, IT’S YOUR LIFE!
TOP TEN REASONS WHY THIS IS NOT JUST A “CLEANING”

10. We make you look better. Healthy teeth and gums are more attractive. Recent studies
show that the smile is the first thing people notice and that people with better looking teeth
are more confident and successful.

9. We can relieve your headaches. During your hygiene visit we evaluate for serious bite
issues, many of which lead to muscle soreness, headaches, and migraines.

8. We check for oral cancer. Oral cancer kills 1 person per hour 24 hours a day. The death rate for oral cancer is higher than cancers we routinely hear about such as cervical, thyroid and skin cancer.

7. We make you smell better. During your hygiene visit we eliminate many of the germs that live under your gum tissue and cause bad breath.

6. We save you money. By utilizing the latest dental technology (digital x-rays, mouth
cameras, and magnification glasses) we can help with early detection of tooth and gum
problems and save you the cost of gum surgery, root canals, and implants.

5. We clean in places you cannot. We clean under the gum line and between teeth where
most of the germs hide and cause dental disease. 40% of the bacteria in your mouth lives in
between your teeth.

4. We prevent pain. We identify tooth decay that can lead to nerve involvement and pain,
root canal, and tooth loss.

3. We save your teeth. Most tooth loss is from periodontal/gum disease. At each visit we
evaluate the health of your gums and bone with our periodontal screening. Periodontal
disease, like high blood pressure, is symptomless until it is in advanced stages.

2. We protect your loved ones. Studies have proven that the bacteria that cause dental
disease can be transmitted from person to person. Think about that the next time you kiss
someone!

1. We prolong life. Researchers have linked the inflammation and infection found in the
mouth to heart attacks, strokes, and Alzheimer’s. By reducing infection in your mouth we can
greatly improve your overall health!

```html
<!DOCTYPE html>
<html lang="en">
<head>
<meta charset="UTF-8">
<title>It's Not a Cleaning, It's Your Life!</title>
<link href="https://fonts.googleapis.com/css2?family=Titillium+Web:wght@300;400;600;700&display=swap" rel="stylesheet">
<style>
  :root {
    --blue: #1fa6e0;
    --band-start: #12aee8;
    --band-mid: #8fa88a;
    --band-end: #f7941d;
    --ink: #1a1a1a;
    --white: #ffffff;
    --lips: #d9262c;
    --pill: #9b1f5f;
    --money: #3ab54a;
    --tools: #a3a3a3;
    --heart: #e8138c;
    --kit: #f05a28;
    --brush: #e8234f;
    --drop: #1b9fe0;
    --tooth: #1c75bc;
    --pulse: #fbb03b;
  }
  * { margin: 0; padding: 0; box-sizing: border-box; }
  html, body { width: 900px; height: 1200px; overflow: hidden; background: var(--white); }
  .poster { position: relative; width: 900px; height: 1200px; font-family: "Titillium Web", sans-serif; color: var(--ink); }

  .headline { position: absolute; left: 191px; top: 192px; display: flex; align-items: flex-start; color: var(--blue); font-weight: 700; }
  .headline-big { font-size: 130px; line-height: 1; letter-spacing: -2px; }
  .headline-small { margin-left: 12px; margin-top: 10px; font-size: 49px; line-height: 47px; letter-spacing: 0.5px; }

  .band { position: absolute; left: 169px; top: 336px; width: 731px; height: 73px;
    background: linear-gradient(90deg, var(--band-start) 0%, var(--band-mid) 50%, var(--band-end) 100%);
    color: var(--white); padding: 13px 0 0 18px; font-size: 19px; line-height: 22px; font-weight: 300; }
  .band strong { font-weight: 700; }

  .reason { position: absolute; width: 240px; font-size: 12.2px; line-height: 14.8px; font-weight: 400; }
  .reason.left { left: 169px; }
  .reason.right { left: 556px; width: 252px; }
  .icon { position: absolute; width: 60px; height: 60px; }
  .icon.left { left: 76px; }
  .icon.right { left: 463px; }
</style>
</head>
<body>
<main class="poster">
  <h1 class="headline">
    <span class="headline-big">IT’S</span>
    <span class="headline-small">NOT A CLEANING,<br>YOUR LIFE!</span>
  </h1>

  <div class="band">TOP TEN REASONS WHY<br>THIS IS NOT JUST A “<strong>CLEANING</strong>”</div>

  <!-- Left column -->
  <svg class="icon left" style="top:450px" viewBox="0 0 60 60" aria-hidden="true">
    <path fill="var(--lips)" d="M2 30 C10 18 20 14 25 19 Q30 22 35 19 C40 14 50 18 58 30 C50 44 40 48 30 48 C20 48 10 44 2 30 Z"/>
    <path fill="#fff" d="M10 30 Q30 34 50 30 Q30 38 10 30 Z"/>
  </svg>
  <p class="reason left" style="top:451px">We make you look better. Healthy teeth and gums are more attractive. Recent studies show that the smile is the first thing people notice and that people with better looking teeth are more confident and successful</p>

  <svg class="icon left" style="top:566px" viewBox="0 0 60 60" aria-hidden="true">
    <g transform="rotate(-45 30 30)">
      <rect x="6" y="20" width="48" height="20" rx="10" fill="none" stroke="var(--pill)" stroke-width="5"/>
      <path d="M30 20 H44 A10 10 0 0 1 44 40 H30 Z" fill="var(--pill)"/>
    </g>
  </svg>
  <p class="reason left" style="top:561px">We check for oral cancer. Oral cancer kills 1 person per hour 24 hours a day. The death rate for oral cancer is higher than cancers we routinely hear about such as cervical, thyroid and skin cancer</p>

  <svg class="icon left" style="top:677px" viewBox="0 0 60 60" aria-hidden="true">
    <text x="30" y="50" text-anchor="middle" font-family="Titillium Web, sans-serif" font-weight="600" font-size="58" fill="var(--money)">$</text>
  </svg>
  <p class="reason left" style="top:671px">We save you money. By utilizing the latest dental technology (digital x-rays, mouth cameras, and magnification glasses) we can help with early detection of tooth and gum problems and save you the cost of gum surgery, root canals, and implants</p>

  <svg class="icon left" style="top:790px" viewBox="0 0 60 60" aria-hidden="true">
    <g fill="var(--tools)">
      <rect x="15" y="24" width="6" height="32" rx="3"/>
      <path d="M18 24 C8 20 10 8 18 6 L20 10 C14 12 15 18 20 20 Z"/>
      <rect x="34" y="24" width="6" height="32" rx="3"/>
      <circle cx="37" cy="14" r="9" fill="none" stroke="var(--tools)" stroke-width="4"/>
    </g>
  </svg>
  <p class="reason left" style="top:793px">We prevent pain. We identify tooth decay that can lead to nerve involvement and pain, root canal, and tooth loss.</p>

  <svg class="icon left" style="top:910px" viewBox="0 0 60 60" aria-hidden="true">
    <path d="M30 52 L8 30 C0 21 6 8 17 8 C23 8 27 12 30 16 C33 12 37 8 43 8 C54 8 60 21 52 30 Z" fill="none" stroke="var(--heart)" stroke-width="5" stroke-linejoin="round"/>
  </svg>
  <p class="reason left" style="top:909px">We protect your loved ones. Studies have proven that the bacteria that cause dental disease can be transmitted from person to person. Think about that the next time you kiss someone!</p>

  <!-- Right column -->
  <svg class="icon right" style="top:450px" viewBox="0 0 60 60" aria-hidden="true">
    <path d="M22 14 V9 H38 V14" fill="none" stroke="var(--kit)" stroke-width="4"/>
    <rect x="2" y="14" width="56" height="40" rx="4" fill="var(--kit)"/>
    <circle cx="30" cy="34" r="11" fill="#fff"/>
    <path d="M27 26 H33 V31 H38 V37 H33 V42 H27 V37 H22 V31 H27 Z" fill="var(--kit)"/>
  </svg>
  <p class="reason right" style="top:451px">We can relieve your headaches. During your hygiene visit we evaluate for serious bite issues, many of which lead to muscle soreness, headaches, and migraines</p>

  <svg class="icon right" style="top:561px" viewBox="0 0 60 60" aria-hidden="true">
    <g transform="rotate(45 30 30)">
      <rect x="26" y="-2" width="10" height="26" rx="3" fill="var(--brush)"/>
      <rect x="29" y="24" width="4" height="34" rx="2" fill="var(--brush)"/>
      <g stroke="#fff" stroke-width="1.5"><line x1="28" y1="4" x2="34" y2="4"/><line x1="28" y1="9" x2="34" y2="9"/><line x1="28" y1="14" x2="34" y2="14"/><line x1="28" y1="19" x2="34" y2="19"/></g>
    </g>
  </svg>
  <p class="reason right" style="top:561px">We make you smell better. During your hygiene visit we eliminate many of the germs that live under your gum tissue and cause bad breath.</p>

  <svg class="icon right" style="top:671px" viewBox="0 0 60 60" aria-hidden="true">
    <path d="M30 2 C22 16 11 28 11 40 A19 19 0 0 0 49 40 C49 28 38 16 30 2 Z" fill="var(--drop)"/>
    <path d="M19 40 A11 11 0 0 0 30 51" fill="none" stroke="#fff" stroke-width="3" stroke-linecap="round"/>
  </svg>
  <p class="reason right" style="top:671px">We clean in places you cannot. We clean under the gum line and between teeth where most of the germs hide and cause dental disease. 40% of the bacteria in your mouth lives in between your teeth.</p>

  <svg class="icon right" style="top:792px" viewBox="0 0 60 60" aria-hidden="true">
    <path d="M18 4 C8 4 4 12 6 22 C8 30 10 36 12 46 C13 54 19 56 21 48 C23 40 25 34 30 34 C35 34 37 40 39 48 C41 56 47 54 48 46 C50 36 52 30 54 22 C56 12 52 4 42 4 C36 4 34 8 30 8 C26 8 24 4 18 4 Z" fill="none" stroke="var(--tooth)" stroke-width="4.5" stroke-linejoin="round"/>
  </svg>
  <p class="reason right" style="top:793px">We save your teeth. Most tooth loss is from periodontal/gum disease. At each visit we evaluate the health of your gums and bone with our periodontal screening. Periodontal disease, like high blood pressure, is symptomless until it is in advanced stages.</p>

  <svg class="icon right" style="top:910px" viewBox="0 0 60 60" aria-hidden="true">
    <circle cx="30" cy="30" r="22" fill="var(--pulse)"/>
    <polyline points="8,31 20,31 24,22 29,42 34,16 38,31 52,31" fill="none" stroke="#fff" stroke-width="3" stroke-linejoin="round"/>
  </svg>
  <p class="reason right" style="top:909px">We prolong life. Researchers have linked the inflammation and infection found in the mouth to heart attacks, strokes, and Alzheimer’s. By reducing infection in your mouth we can greatly improve your overall health!</p>
</main>
</body>
</html>
```